new signage design for budget motel - Brookfern Lodge

renaming the budget motel as Brookfern Lodge, property located on side of a hill. therefore i choose to name is Brookfern Lodge, im looking for clean, modern look in signage design,this property does not have a Logo, plan to us signage design as a logo as well. current pole sign housing is rectangle shape and will be using same housing I'll be attaching picture of the signage for better idea. looking forward to awesome creative designs.

Industry/Entity Type

Motel

Font styles to use
Serif
Sans Serif

Requirements
Should not have
• mountains , mountain(s) with snow , trees, no black color, red color, blue letters, too much green.

```html
<!DOCTYPE html>
<html lang="en">
<head>
<meta charset="utf-8">
<title>Brookfern Lodge – Pole Sign</title>
<link rel="stylesheet" href="https://fonts.googleapis.com/css2?family=Marcellus&display=swap">
<style>
  :root {
    --page-bg: #efefef;
    --sign-teal: #03627f;
    --sign-teal-deep: #045872;
    --gold: #e2bd31;
    --gold-soft: rgba(226, 189, 49, 0.22);
    --shadow: rgba(0, 0, 0, 0.28);
  }
  * { box-sizing: border-box; margin: 0; padding: 0; }
  html, body {
    width: 1000px;
    height: 1200px;
    overflow: hidden;
    background: var(--page-bg);
  }
  .canvas {
    position: relative;
    width: 1000px;
    height: 1200px;
  }
  .sign-panel {
    position: absolute;
    left: 50px;
    top: 417px;
    width: 900px;
    height: 365px;
    border-radius: 22px;
    background: var(--sign-teal);
    box-shadow: 0 8px 18px var(--shadow);
    overflow: hidden;
  }
  .background-pattern {
    position: absolute;
    inset: 0;
    background: radial-gradient(ellipse at center, var(--sign-teal) 0%, var(--sign-teal-deep) 100%);
  }
  .sign-frame {
    position: absolute;
    inset: 0;
  }
  .crest-ornament {
    position: absolute;
    left: 330px;
    top: 32px;
    width: 240px;
    height: 94px;
    border-radius: 47px;
    background: radial-gradient(ellipse at center, var(--gold-soft) 0%, rgba(226, 189, 49, 0) 72%);
  }
  .footer-ornament {
    position: absolute;
    left: 360px;
    top: 252px;
    width: 180px;
    height: 76px;
    border-radius: 38px;
    background: radial-gradient(ellipse at center, var(--gold-soft) 0%, rgba(226, 189, 49, 0) 72%);
  }
  .rule {
    position: absolute;
    left: 236px;
    width: 428px;
    height: 2px;
    background: var(--gold);
  }
  .rule--top { top: 134px; }
  .rule--bottom { top: 244px; }
  .sign-name {
    position: absolute;
    left: 0;
    right: 0;
    top: 150px;
    text-align: center;
    font-family: "Marcellus", "Times New Roman", serif;
    font-weight: 400;
    font-size: 62px;
    line-height: 80px;
    letter-spacing: 1px;
    color: var(--gold);
  }
</style>
</head>
<body>
  <main class="canvas">
    <section class="sign-panel" aria-label="Brookfern Lodge pole sign">
      <div class="background-pattern" role="img" aria-label="Subtle tone-on-tone overlapping circle pattern across the teal panel"></div>

      <svg class="sign-frame" width="900" height="365" viewBox="0 0 900 365" aria-hidden="true">
        <path d="M30 16 H870 A14 14 0 0 0 884 30 V335 A14 14 0 0 0 870 349 H30 A14 14 0 0 0 16 335 V30 A14 14 0 0 0 30 16 Z"
              fill="none" stroke="var(--gold)" stroke-width="2"/>
        <path d="M33 20 H867 A13 13 0 0 0 880 33 V332 A13 13 0 0 0 867 345 H33 A13 13 0 0 0 20 332 V33 A13 13 0 0 0 33 20 Z"
              fill="none" stroke="var(--gold)" stroke-width="0.8"/>
      </svg>

      <div class="crest-ornament" role="img" aria-label="Gold scrollwork crest with an oval monogram and dotted crown"></div>
      <div class="rule rule--top"></div>

      <h1 class="sign-name">BROOKFERN LODGE</h1>

      <div class="rule rule--bottom"></div>
      <div class="footer-ornament" role="img" aria-label="Gold scrollwork flourish with a small bell motif and dotted trim"></div>
    </section>
  </main>
</body>
</html>
```